Consulting firm need a professional powerpoint design

A startup Climate change firm needs a powerpoint template design. The design should reflect aspects of climate change adaptation, resilience and environmental sustainability.

The powerpoint design must convey aspects of nature and climate action for a resilient society.

The last slide of the powerpoint must have a allocation for a slogan such as 'Linking science and decision-making'.

Use the colors in the logo and business card for the powerpoint design.

Target Market(s)

Government and industry

Font styles to use
Sans Serif
Other font styles liked:
• nexa font family

Colors
85cae6
abd037
fece3e

Requirements
Must have
• - Colors used in logo and business card
- Convey science and nature
- Professional
Nice to have
• Many pages
Should not have
• Not complicated

```html
<!DOCTYPE html>
<html lang="en">
<head>
<meta charset="utf-8">
<title>Terravera Presentation Deck</title>
<link rel="stylesheet" href="https://fonts.googleapis.com/css2?family=Montserrat:wght@400;500;600;700;800&display=swap">
<style>
:root{--navy:#1b2b4b;--navy2:#25395f;--green:#5db335;--lime:#abd037;--yellow:#fece3e;--orange:#f5a11c;--sky:#85cae6;--blue:#1d9ad6;--ink:#2b2b2b;--muted:#777;--page:#e6e7e9;--panel:#f1f2f4}
*{box-sizing:border-box}
html,body{margin:0;padding:0}
body{width:1200px;height:2338px;overflow:hidden;position:relative;background:var(--page);font-family:'Montserrat',sans-serif;color:var(--ink)}
.hero{position:absolute;left:0;top:0;width:1200px;height:490px;background:linear-gradient(160deg,#b4ab9b 0%,#9c968c 30%,#c9c8c5 55%,var(--page) 72%)}
.hero-title{position:absolute;left:71px;top:180px;margin:0;line-height:1}
.hero-title .a{display:block;font-size:60px;font-weight:800;color:var(--green)}
.hero-title .b{display:block;font-size:60px;font-weight:500;color:#1f1f1f;margin-left:127px;margin-top:2px}
.hero-screen{position:absolute;left:562px;top:86px;transform:scale(1.222);transform-origin:0 0;box-shadow:0 6px 20px rgba(0,0,0,.25)}
.slide{position:absolute;width:384px;height:216px;background:#fff;overflow:hidden}
.c1{left:13px}.c2{left:408px}.c3{left:803px}
.r1{top:497px}.r2{top:727px}.r3{top:962px}.r4{top:1191px}.r5{top:1421px}.r6{top:1650px}.r7{top:1879px}.r8{top:2109px}
.ph{position:absolute}
.bar{position:absolute;left:0;top:0;right:0;height:30px;background:var(--navy)}
.bar h3{margin:0;position:absolute;left:8px;top:5px;color:#fff;font-size:9px;font-weight:700;letter-spacing:-.1px}
.bar small{position:absolute;left:8px;top:16px;color:var(--yellow);font-size:4.5px;letter-spacing:1.2px;font-weight:700}
.stripe{position:absolute;left:0;right:0;height:2px;background:linear-gradient(90deg,var(--navy) 0 38%,var(--green) 38% 58%,var(--yellow) 58% 74%,var(--blue) 74%)}
.bar .stripe{bottom:-3px}
.brand{position:absolute;right:9px;top:10px;display:flex;align-items:center;gap:3px;font-size:6.5px;font-weight:700;color:#fff;letter-spacing:.4px}
.brand i{display:block;width:7px;height:7px;border-radius:50%;background:var(--lime)}
.brand.dark{color:var(--navy)}
.foot{position:absolute;left:0;right:0;bottom:0;height:8px;background:var(--navy);color:#fff;font-size:3.4px;padding-left:10px;line-height:8px}
.foot .stripe{top:-2px}
.tx{font-size:4px;line-height:1.45;color:var(--muted);margin:0}
.hd{font-size:5.2px;font-weight:700;color:var(--navy);margin:0 0 1px}
.dot{position:absolute;border-radius:50%;display:flex;align-items:center;justify-content:center;color:#fff;font-weight:700}
.abs{position:absolute}
.t-big{position:absolute;margin:0;color:var(--navy);line-height:1}
.t-big .l1{display:block;font-size:13px;font-weight:500}
.t-big .l2{display:block;font-size:25px;font-weight:400;letter-spacing:1.5px;margin-top:3px}
.t-big .l3{display:block;font-size:6px;letter-spacing:2.6px;margin-top:5px}
.year{position:absolute;font-size:7px;letter-spacing:3px}
.toc{position:absolute;left:228px;top:38px;margin:0;padding:0;list-style:none;font-size:5.6px;color:#888}
.toc li{height:15.5px;display:flex}
.toc b{width:24px;font-weight:400}
.navybox{position:absolute;background:var(--navy);border-radius:6px;color:#fff;font-size:6px;font-weight:700;text-align:center;display:flex;align-items:center;justify-content:center;padding:8px;box-shadow:0 3px 6px rgba(0,0,0,.25)}
.card{position:absolute;top:57px;width:88px;height:136px;border-radius:8px;text-align:center;color:#fff}
.card .ic{width:48px;height:48px;border-radius:50%;background:#fff;margin:10px auto 0}
.card h4{font-size:5px;margin:22px 0 3px;color:#fff8d0}
.card p{font-size:3.8px;line-height:1.45;margin:0 8px}
.label{position:absolute;left:30px;width:66px;height:18px;color:#fff;font-size:4.5px;font-weight:600;display:flex;align-items:center;justify-content:center}
.grid-tab{position:absolute;border-collapse:collapse;font-size:4px;color:#444}
.grid-tab td,.grid-tab th{text-align:center;height:13px}
.grid-tab th{font-weight:600;color:var(--navy);border-top:1px solid var(--navy);border-bottom:1px solid var(--navy)}
.grid-tab tr:nth-child(odd) td{background:#eef0f3}
.step{position:absolute;height:11px;background:var(--navy);color:#fff;font-size:5px;font-weight:700;text-align:right;padding-right:4px;line-height:11px}
.team{position:absolute;top:50px;width:80px;height:138px;background:var(--panel);padding:6px 8px;border-bottom:2px solid var(--green)}
.team .pic{width:24px;height:24px;border-radius:50%;background:linear-gradient(#9aa0a8,#5e646c)}
.team h5{margin:6px 0 0;font-size:5.5px;color:var(--navy);font-weight:600}
.team h6{margin:0 0 5px;font-size:5px;font-weight:400;color:#555}
</style>
</head>
<body>

<section class="hero">
  <div class="ph" style="inset:0;background:linear-gradient(155deg,rgba(205,160,110,.55),rgba(120,115,108,.2) 45%,rgba(230,231,233,0) 70%)" role="img" aria-label="Faded photograph of a cheering crowd at a climate rally at sunset"></div>
  <h1 class="hero-title"><span class="a">Presentation</span><span class="b">Deck</span></h1>

  <div class="slide hero-screen">
    <div class="ph" style="left:0;top:0;width:200px;height:216px;background:linear-gradient(90deg,#8f969b,#c9c3b6 55%,rgba(255,255,255,0))" role="img" aria-label="Photograph of a protest sign about the planet, with a colourful curved brand graphic"></div>
    <div class="brand dark" style="left:200px;right:auto;top:70px;font-size:10px"><i style="width:11px;height:11px"></i>TERRAVERA</div>
    <h2 class="t-big" style="left:200px;top:106px"><span class="l1">ADD YOUR AWESOME</span><span class="l2">TITLE HERE</span><span class="l3">HERE ADD YOUR SUBTITLE</span></h2>
    <span class="year" style="left:203px;top:189px">2020</span>
  </div>
</section>

<!-- row 1 -->
<div class="slide c1 r1">
  <div class="ph" style="left:0;top:0;width:200px;height:216px;background:linear-gradient(90deg,#8f969b,#c9c3b6 55%,rgba(255,255,255,0))" role="img" aria-label="Photograph of a protest sign about the planet, with a colourful curved brand graphic"></div>
  <div class="brand dark" style="left:200px;right:auto;top:70px;font-size:10px"><i style="width:11px;height:11px"></i>TERRAVERA</div>
  <h2 class="t-big" style="left:200px;top:106px"><span class="l1">ADD YOUR AWESOME</span><span class="l2">TITLE HERE</span><span class="l3">HERE ADD YOUR SUBTITLE</span></h2>
  <span class="year" style="left:203px;top:189px">2020</span>
</div>

<div class="slide c2 r1" style="background:var(--navy)">
  <div class="ph" style="inset:0;background:linear-gradient(180deg,#2c4068,#1b2b4b 60%,#3a4a62)" role="img" aria-label="Dusky landscape photograph with a wind turbine"></div>
  <div class="brand" style="left:132px;right:auto;top:58px;font-size:10px"><i style="width:11px;height:11px"></i>TERRAVERA</div>
  <h2 class="t-big" style="left:0;right:0;top:96px;text-align:center;color:#fff"><span class="l1">ADD YOUR AWESOME</span><span class="l2">TITLE HERE</span><span class="l3">HERE ADD YOUR SUBTITLE</span></h2>
  <span class="year" style="left:180px;top:200px;color:#fff;font-size:5px">2020</span>
</div>

<div class="slide c3 r1">
  <div class="ph" style="left:0;top:0;width:118px;height:216px;background:linear-gradient(180deg,#3a2414,#a0561f 55%,#2a1a10)" role="img" aria-label="Photograph of hands holding a glowing globe"></div>
  <div class="brand" style="left:22px;right:auto;top:112px"><i></i>TERRAVERA</div>
  <div class="abs" style="left:118px;top:0;width:26px;height:216px;background:var(--navy)"></div>
  <div class="abs" style="left:124px;top:184px;transform:rotate(-90deg);transform-origin:0 0;color:#fff;font-size:12px;font-weight:700;white-space:nowrap">TABLE OF CONTENTS</div>
  <ol class="toc">
    <li><b>i.</b>Introduction</li><li><b>ii.</b>About Us</li><li><b>iii.</b>Welcome Message</li><li><b>iv.</b>Company Profile</li><li><b>v.</b>Team</li><li><b>vi.</b>Team Group</li><li><b>vii.</b>Portfolio</li><li><b>viii.</b>Info graphic</li><li><b>ix.</b>Contact Us</li><li><b>x.</b>Data Chart</li>
  </ol>
</div>

<!-- row 2 -->
<div class="slide c1 r2">
  <div class="abs" style="left:0;right:0;top:0;height:20px;background:#fff;border-bottom:4px solid var(--navy)"></div>
  <div class="stripe" style="top:24px"></div>
  <div class="brand dark" style="top:6px"><i></i>TERRAVERA</div>
  <div class="abs" style="left:18px;top:52px;width:348px">
    <p class="hd" style="font-size:5.5px;margin-bottom:14px">Lorem ipsum dolor sit amet, consectetur adipiscing elit.</p>
    <p class="tx">Fusce sit amet neque sodales, faucibus ex eu, efficitur lacus. Cras imperdiet, nulla nec sagittis pulvinar, neque augue iaculis risus, ac fringilla felis urna fermentum mi. Ut vehicula vel enim sit amet vulputate. Aenean malesuada consectetur diam, ac convallis quam tincidunt eget. Nam vitae elementum ipsum. Proin vitae blandit enim. Donec congue convallis commodo. Aenean vel lacus lacus. Sed in erat ultrices dolor faucibus feugiat. Nullam cursus sollicitudin dictum. Donec a ex et enim consectetur auctor. Aliquam ut laoreet neque, in viverra nunc porta sodales diam. Sed ullamcorper et ante eget euismod. Sed in erat ultrices dolor faucibus feugiat. Nullam cursus sollicitudin dictum. Donec a ex at enim consectetur auctor. Aliquam ut laoreet neque.</p>
    <p class="tx" style="margin-top:8px">Maecenas in purus et tellus tincidunt sodales eu sed nibh. Aenean justo diam, commodo vel felis ac, malesuada sodales purus. Nunc sollicitudin sed justo in efficitur. Fusce dictum ornare ligula, eu lacinia nunc dignissim non. Aliquam erat volutpat. Mauris malesuada turpis non tellus scelerisque tempus. Morbi dui turpis, mollis a ultrices blandit, commodo a enim. Mauris sit amet eleifend sapien.</p>
  </div>
  <div class="foot"><div class="stripe"></div>Copyright © 2020 Terravera | All rights reserved</div>
</div>

<div class="slide c2 r2">
  <div class="ph" style="left:0;top:0;width:146px;height:216px;background:linear-gradient(180deg,#8c8f8e,#b7a77c 45%,#d9b324)" role="img" aria-label="Photograph of a protester in a yellow raincoat holding a Save our planet sign"></div>
  <div class="brand dark"><i></i>TERRAVERA</div>
  <div class="abs" style="left:120px;top:28px;width:180px;height:32px;background:var(--navy);color:var(--yellow);font-size:8px;font-weight:600;display:flex;align-items:center;justify-content:center">LOREM IPSUM CONSECTETUR</div>
  <p class="tx" style="position:absolute;left:180px;top:83px;width:180px">Business valuation is a process and a set of procedures used to estimate the economic value of an owner's interest in a business. Valuation is used by financial market participants to determine the price they are willing to pay or receive to effect a sale of a business.</p>
  <svg class="abs" style="left:180px;top:122px" width="10" height="10" viewBox="0 0 10 10"><path d="M1 9h8M2 7l5-5 1.5 1.5-5 5H2z" fill="none" stroke="#f5a11c" stroke-width="1"/></svg>
  <svg class="abs" style="left:276px;top:122px" width="10" height="10" viewBox="0 0 10 10"><path d="M1 5 9 1 6 9 5 6z" fill="#1b2b4b"/></svg>
  <div class="abs" style="left:180px;top:138px;width:88px"><p class="hd" style="color:var(--orange);font-weight:500">Your Contents Here</p><p class="tx">Lorem ipsum dolor sit amet, consectetur adipiscing elit, sed do eiusmod tempor incididunt.</p></div>
  <div class="abs" style="left:276px;top:138px;width:88px"><p class="hd" style="color:var(--orange);font-weight:500">Your Contents Here</p><p class="tx">Lorem ipsum dolor sit amet, consectetur adipiscing elit, sed do eiusmod tempor incididunt.</p></div>
  <div class="foot"><div class="stripe"></div>Copyright © 2020 Terravera | All rights reserved</div>
</div>

<div class="slide c3 r2">
  <div class="bar"><h3>TWO BULLET POINTS</h3><small>HERE ADD YOUR TITLE</small><div class="brand"><i></i>TERRAVERA</div><div class="stripe"></div></div>
  <div class="navybox" style="left:40px;top:87px;width:138px;height:64px">Lorem Ipsum is simply dummy unknown printer took a galley of type and scrambled it to make.</div>
  <div class="navybox" style="left:212px;top:87px;width:138px;height:64px">Lorem Ipsum is simply dummy unknown printer took a galley of type and scrambled it to make.</div>
  <div class="foot"><div class="stripe"></div>Copyright © 2020 Terravera | All rights reserved</div>
</div>

<!-- row 3 -->
<div class="slide c1 r3">
  <div class="bar"><h3>FOUR BULLET POINTS AND PICTURE</h3><small>HERE ADD YOUR TITLE</small><div class="brand"><i></i>TERRAVERA</div><div class="stripe"></div></div>
  <div class="dot" style="left:30px;top:57px;width:20px;height:20px;background:var(--green);font-size:7px">✓</div>
  <div class="dot" style="left:30px;top:92px;width:20px;height:20px;background:var(--green);font-size:7px">✓</div>
  <div class="dot" style="left:30px;top:127px;width:20px;height:20px;background:var(--green);font-size:7px">✓</div>
  <div class="dot" style="left:30px;top:162px;width:20px;height:20px;background:var(--green);font-size:7px">✓</div>
  <div class="abs" style="left:62px;top:56px;width:90px"><p class="hd">Your Text Here</p><p class="tx">Lorem ipsum dolor sit amet, nec an dictas equidem appetere, ut has commune accommodare.</p></div>
  <div class="abs" style="left:62px;top:91px;width:90px"><p class="hd">Your Text Here</p><p class="tx">Lorem ipsum dolor sit amet, nec an dictas equidem appetere, ut has commune accommodare.</p></div>
  <div class="abs" style="left:62px;top:126px;width:90px"><p class="hd">Your Text Here</p><p class="tx">Lorem ipsum dolor sit amet, nec an dictas equidem appetere, ut has commune accommodare.</p></div>
  <div class="abs" style="left:62px;top:161px;width:90px"><p class="hd">Your Text Here</p><p class="tx">Lorem ipsum dolor sit amet, nec an dictas equidem appetere, ut has commune accommodare.</p></div>
  <div class="ph" style="left:212px;top:48px;width:150px;height:145px;background:linear-gradient(160deg,#e6f2d8,#d8ecf5)" role="img" aria-label="Illustration of the Earth with green leaves sprouting"></div>
  <div class="foot"><div class="stripe"></div>Copyright © 2020 Terravera | All rights reserved</div>
</div>

<div class="slide c2 r3">
  <div class="bar"><h3>ADD YOUR AWESOME TITLE HERE</h3><small>HERE ADD YOUR TITLE</small><div class="brand"><i></i>TERRAVERA</div><div class="stripe"></div></div>
  <div class="dot" style="left:17px;top:60px;width:16px;height:16px;background:var(--green);font-size:5.5px">1</div>
  <div class="dot" style="left:17px;top:97px;width:16px;height:16px;background:var(--green);font-size:5.5px">2</div>
  <div class="dot" style="left:17px;top:134px;width:16px;height:16px;background:var(--green);font-size:5.5px">3</div>
  <div class="dot" style="left:17px;top:171px;width:16px;height:16px;background:var(--green);font-size:5.5px">4</div>
  <div class="abs" style="left:42px;top:54px;width:80px"><p class="hd">Contents Title</p><p class="tx">Lorem ipsum randomised words which in some form, by injected humour.</p></div>
  <div class="abs" style="left:42px;top:91px;width:80px"><p class="hd">Contents Title</p><p class="tx">Lorem ipsum randomised words which in some form, by injected humour.</p></div>
  <div class="abs" style="left:42px;top:128px;width:80px"><p class="hd">Contents Title</p><p class="tx">Lorem ipsum randomised words which in some form, by injected humour.</p></div>
  <div class="abs" style="left:42px;top:165px;width:80px"><p class="hd">Contents Title</p><p class="tx">Lorem ipsum randomised words which in some form, by injected humour.</p></div>
  <div class="ph" style="left:140px;top:80px;width:80px;height:128px;background:linear-gradient(180deg,#e4f1d6,#f3f7ee)" role="img" aria-label="Illustration of a green tree"></div>
  <div class="dot" style="left:252px;top:60px;width:16px;height:16px;background:#8a8a8a;font-size:5.5px">1</div>
  <div class="dot" style="left:252px;top:97px;width:16px;height:16px;background:#8a8a8a;font-size:5.5px">2</div>
  <div class="dot" style="left:252px;top:134px;width:16px;height:16px;background:#8a8a8a;font-size:5.5px">3</div>
  <div class="dot" style="left:252px;top:171px;width:16px;height:16px;background:#8a8a8a;font-size:5.5px">4</div>
  <div class="abs" style="left:277px;top:54px;width:80px"><p class="hd">Contents Title</p><p class="tx">Lorem ipsum randomised words which in some form, by injected humour.</p></div>
  <div class="abs" style="left:277px;top:91px;width:80px"><p class="hd">Contents Title</p><p class="tx">Lorem ipsum randomised words which in some form, by injected humour.</p></div>
  <div class="abs" style="left:277px;top:128px;width:80px"><p class="hd">Contents Title</p><p class="tx">Lorem ipsum randomised words which in some form, by injected humour.</p></div>
  <div class="abs" style="left:277px;top:165px;width:80px"><p class="hd">Contents Title</p><p class="tx">Lorem ipsum randomised words which in some form, by injected humour.</p></div>
  <div class="foot"><div class="stripe"></div>Copyright © 2020 Terravera | All rights reserved</div>
</div>

<div class="slide c3 r3">
  <div class="bar"><h3>SIX POINTS</h3><small>HERE ADD YOUR TITLE</small><div class="brand"><i></i>TERRAVERA</div><div class="stripe"></div></div>
  <div class="dot" style="left:22px;top:87px;width:15px;height:15px;background:var(--green);font-size:4.5px">01</div>
  <div class="dot" style="left:142px;top:89px;width:15px;height:15px;background:var(--green);font-size:4.5px">02</div>
  <div class="dot" style="left:266px;top:89px;width:15px;height:15px;background:var(--green);font-size:4.5px">03</div>
  <div class="dot" style="left:22px;top:139px;width:15px;height:15px;background:var(--green);font-size:4.5px">04</div>
  <div class="dot" style="left:142px;top:139px;width:15px;height:15px;background:var(--green);font-size:4.5px">05</div>
  <div class="dot" style="left:266px;top:139px;width:15px;height:15px;background:var(--green);font-size:4.5px">06</div>
  <div class="abs" style="left:45px;top:78px;width:82px"><p class="hd">Project name</p><p class="tx">Lorem ipsum is simply dummy unknown printer took a galley of type.</p></div>
  <div class="abs" style="left:164px;top:80px;width:82px"><p class="hd">Project name</p><p class="tx">Lorem ipsum is simply dummy unknown printer took a galley of type.</p></div>
  <div class="abs" style="left:288px;top:80px;width:82px"><p class="hd">Project name</p><p class="tx">Lorem ipsum is simply dummy unknown printer took a galley of type.</p></div>
  <div class="abs" style="left:45px;top:130px;width:82px"><p class="hd">Project name</p><p class="tx">Lorem ipsum is simply dummy unknown printer took a galley of type.</p></div>
  <div class="abs" style="left:164px;top:130px;width:82px"><p class="hd">Project name</p><p class="tx">Lorem ipsum is simply dummy unknown printer took a galley of type.</p></div>
  <div class="abs" style="left:288px;top:130px;width:82px"><p class="hd">Project name</p><p class="tx">Lorem ipsum is simply dummy unknown printer took a galley of type.</p></div>
  <div class="foot"><div class="stripe"></div>Copyright © 2020 Terravera | All rights reserved</div>
</div>

<!-- row 4 -->
<div class="slide c1 r4">
  <div class="abs" style="left:42px;top:31px;width:40px;height:2px;background:var(--navy)"></div>
  <p class="abs" style="left:42px;top:36px;width:128px;margin:0;font-size:8.3px;font-weight:500;color:var(--navy);line-height:1.3;text-align:justify">Success is not only what you achieve in your life, but also what you inspire in the lives of others</p>
  <div class="ph" style="left:0;top:108px;width:384px;height:108px;background:linear-gradient(90deg,#1b2b4b,#24385e 60%,#2f3f5a)" role="img" aria-label="Dark navy tinted photograph of a landscape"></div>
  <div class="abs" style="left:35px;top:138px;width:100px;color:#fff"><p style="margin:0 0 10px;font-size:5.5px;font-weight:700">Lorem ipsum dolor</p><p class="tx" style="color:#d6dbe4">Lorem ipsum dolor sit amet, consectetur adipiscing elit, sed do eiusmod tempor</p></div>
  <div class="abs" style="left:148px;top:138px;width:100px;color:#fff"><p style="margin:0 0 10px;font-size:5.5px;font-weight:700">Lorem ipsum dolor</p><p class="tx" style="color:#d6dbe4">Lorem ipsum dolor sit amet, consectetur adipiscing elit, sed do eiusmod tempor</p></div>
  <div class="abs" style="left:258px;top:138px;width:100px;color:#fff"><p style="margin:0 0 10px;font-size:5.5px;font-weight:700">Lorem ipsum dolor</p><p class="tx" style="color:#d6dbe4">Lorem ipsum dolor sit amet, consectetur adipiscing elit, sed do eiusmod tempor</p></div>
</div>

<div class="slide c2 r4">
  <div class="bar"><h3>ADD YOUR AWESOME TITLE HERE</h3><small>HERE ADD YOUR TITLE</small><div class="brand"><i></i>TERRAVERA</div><div class="stripe"></div></div>
  <div class="card" style="left:49px;background:linear-gradient(160deg,#fece3e,#f5a11c)"><div class="ic"></div><h4>Your Contents Here</h4><p>Lorem ipsum dolor sit amet, consectetur adipiscing elit, sed do eiusmod tempor incididunt.</p></div>
  <div class="card" style="left:148px;background:linear-gradient(160deg,#abd037,#5db335)"><div class="ic"></div><h4>Your Contents Here</h4><p>Lorem ipsum dolor sit amet, consectetur adipiscing elit, sed do eiusmod tempor incididunt.</p></div>
  <div class="card" style="left:247px;background:linear-gradient(160deg,#85cae6,#1d9ad6)"><div class="ic"></div><h4>Your Contents Here</h4><p>Lorem ipsum dolor sit amet, consectetur adipiscing elit, sed do eiusmod tempor incididunt.</p></div>
  <div class="foot"><div class="stripe"></div>Copyright © 2020 Terravera | All rights reserved</div>
</div>

<div class="slide c3 r4">
  <div class="bar"><h3>TIMELINE</h3><small>HERE ADD YOUR TITLE</small><div class="brand"><i></i>TERRAVERA</div><div class="stripe"></div></div>
  <div class="abs" style="left:38px;top:97px;width:310px;height:1px;background:#ccc"></div>
  <div class="dot" style="left:33px;top:92px;width:10px;height:10px;background:var(--lime)"></div>
  <div class="dot" style="left:95px;top:92px;width:10px;height:10px;background:var(--blue)"></div>
  <div class="dot" style="left:157px;top:92px;width:10px;height:10px;background:var(--yellow)"></div>
  <div class="dot" style="left:219px;top:92px;width:10px;height:10px;background:var(--lime)"></div>
  <div class="dot" style="left:281px;top:92px;width:10px;height:10px;background:var(--blue)"></div>
  <div class="dot" style="left:343px;top:92px;width:10px;height:10px;background:var(--yellow)"></div>
  <div class="abs" style="left:7px;top:80px;width:372px;display:flex;font-size:5.5px;font-weight:700;color:var(--navy)"><span style="width:62px;text-align:center">2015</span><span style="width:62px;text-align:center">2016</span><span style="width:62px;text-align:center">2017</span><span style="width:62px;text-align:center">2018</span><span style="width:62px;text-align:center">2019</span><span style="width:62px;text-align:center">2020</span></div>
  <div class="abs" style="left:7px;top:128px;width:372px;display:flex;text-align:center">
    <div style="width:62px;padding:0 3px"><p class="hd">Project name</p><p class="tx">Lorem ipsum is simply dummy unknown printer.</p></div>
    <div style="width:62px;padding:0 3px"><p class="hd">Project name</p><p class="tx">Lorem ipsum is simply dummy unknown printer.</p></div>
    <div style="width:62px;padding:0 3px"><p class="hd">Project name</p><p class="tx">Lorem ipsum is simply dummy unknown printer.</p></div>
    <div style="width:62px;padding:0 3px"><p class="hd">Project name</p><p class="tx">Lorem ipsum is simply dummy unknown printer.</p></div>
    <div style="width:62px;padding:0 3px"><p class="hd">Project name</p><p class="tx">Lorem ipsum is simply dummy unknown printer.</p></div>
    <div style="width:62px;padding:0 3px"><p class="hd">Project name</p><p class="tx">Lorem ipsum is simply dummy unknown printer.</p></div>
  </div>
  <div class="foot"><div class="stripe"></div>Copyright © 2020 Terravera | All rights reserved</div>
</div>

<!-- row 5 -->
<div class="slide c1 r5">
  <div class="bar"><h3>INFOGRAPHIC</h3><small>HERE ADD YOUR TITLE</small><div class="brand"><i></i>TERRAVERA</div><div class="stripe"></div></div>
  <svg class="abs" style="left:135px;top:63px" width="112" height="112" viewBox="0 0 112 112"><circle cx="56" cy="56" r="52" fill="none" stroke="#aab" stroke-dasharray="2 2" stroke-width=".6"/></svg>
  <div class="dot" style="left:150px;top:78px;width:82px;height:82px;background:var(--navy);font-size:7px;text-align:center;line-height:1.2">Add Your<br>Awesome Title<br>Here</div>
  <div class="dot" style="left:142px;top:83px;width:8px;height:8px;border:1.5px solid var(--lime);background:#fff"></div>
  <div class="dot" style="left:137px;top:115px;width:8px;height:8px;border:1.5px solid var(--green);background:#fff"></div>
  <div class="dot" style="left:142px;top:148px;width:8px;height:8px;border:1.5px solid var(--blue);background:#fff"></div>
  <div class="dot" style="left:234px;top:83px;width:8px;height:8px;border:1.5px solid var(--blue);background:#fff"></div>
  <div class="dot" style="left:239px;top:115px;width:8px;height:8px;border:1.5px solid var(--green);background:#fff"></div>
  <div class="dot" style="left:234px;top:148px;width:8px;height:8px;border:1.5px solid var(--orange);background:#fff"></div>
  <div class="label" style="left:62px;top:74px;width:62px;height:24px;background:linear-gradient(var(--yellow),var(--orange));font-weight:400;font-size:3.8px">Composition of the Board</div>
  <div class="label" style="left:54px;top:109px;width:62px;height:24px;background:linear-gradient(var(--lime),var(--green));font-weight:400;font-size:3.8px">Clarity of roles</div>
  <div class="label" style="left:62px;top:144px;width:62px;height:24px;background:linear-gradient(var(--sky),var(--blue));font-weight:400;font-size:3.8px">Joint vision</div>
  <div class="label" style="left:258px;top:74px;width:62px;height:24px;background:linear-gradient(var(--sky),var(--blue));font-weight:400;font-size:3.8px">Ability to use the strengths of all</div>
  <div class="label" style="left:258px;top:109px;width:68px;height:24px;background:linear-gradient(var(--lime),var(--green));font-weight:400;font-size:3.8px">Ability to resolve conflicts</div>
  <div class="label" style="left:258px;top:144px;width:62px;height:24px;background:linear-gradient(var(--yellow),var(--orange));font-weight:400;font-size:3.8px">Structure of the work</div>
  <div class="foot"><div class="stripe"></div>Copyright © 2020 Terravera | All rights reserved</div>
</div>

<div class="slide c2 r5">
  <div class="ph" style="left:80px;top:8px;width:300px;height:186px;background:linear-gradient(180deg,#e9ecf2,#dde2ea)" role="img" aria-label="World map with highlighted locations"></div>
  <div class="brand dark"><i></i>TERRAVERA</div>
  <p class="abs" style="left:24px;top:147px;margin:0;font-size:11.5px;color:var(--navy);line-height:1.3">Add Your<br>Awesome<br>Title Here</p>
  <div class="foot"><div class="stripe"></div>Copyright © 2020 Terravera | All rights reserved</div>
</div>

<div class="slide c3 r5">
  <p class="abs" style="left:0;right:0;top:11px;margin:0;text-align:center;font-size:12px;color:var(--navy)">OUR TEAM</p>
  <p class="abs" style="left:0;right:0;top:27px;margin:0;text-align:center;font-size:4.5px;letter-spacing:1.3px;color:var(--blue);font-weight:700">HERE ADD YOUR TITLE</p>
  <div class="brand dark"><i></i>TERRAVERA</div>
  <div class="team" style="left:12px;background:#fff"><div class="pic" role="img" aria-label="Portrait photo of a team member"></div><h5>Your Name</h5><h6>Founder</h6><p class="tx">Lorem ipsum dolor sit amet, consectetur adipiscing elit. Donec mauris lorem, vestibulum ac rutrum id, suscipit in dui.</p></div>
  <div class="team" style="left:100px"><div class="pic" role="img" aria-label="Portrait photo of a team member"></div><h5>Your Name</h5><h6>Global Account Executive</h6><p class="tx">Lorem ipsum dolor sit amet, consectetur adipiscing elit. Donec mauris lorem, vestibulum ac rutrum id.</p></div>
  <div class="team" style="left:194px;background:#fff"><div class="pic" role="img" aria-label="Portrait photo of a team member"></div><h5>Your Name</h5><h6>Founder</h6><p class="tx">Lorem ipsum dolor sit amet, consectetur adipiscing elit. Donec mauris lorem, vestibulum ac rutrum id, suscipit in dui.</p></div>
  <div class="team" style="left:284px"><div class="pic" role="img" aria-label="Portrait photo of a team member"></div><h5>Your Name</h5><h6>Global Account Executive</h6><p class="tx">Lorem ipsum dolor sit amet, consectetur adipiscing elit. Donec mauris lorem, vestibulum ac rutrum id.</p></div>
  <div class="foot"><div class="stripe"></div>Copyright © 2020 Terravera | All rights reserved</div>
</div>

<!-- row 6 -->
<div class="slide c1 r6">
  <div class="bar"><h3>YOUR AWESOME TEXT HERE</h3><small>HERE ADD YOUR TITLE</small><div class="brand"><i></i>TERRAVERA</div><div class="stripe"></div></div>
  <div class="label" style="top:61px;background:var(--yellow)">Business valuation</div>
  <div class="label" style="top:90px;background:var(--green)">Business valuation</div>
  <div class="label" style="top:119px;background:var(--yellow)">Business valuation</div>
  <div class="label" style="top:148px;background:var(--green)">Business valuation</div>
  <p class="tx abs" style="left:102px;top:60px;width:262px;border-bottom:.5px solid #ccc;padding-bottom:2px">Lorem ipsum dolor sit amet, consectetur adipiscing elit, sed do eiusmod tempor incididunt ut labore et dolore magna aliqua. Ut enim ad minim veniam, quis nostrud exercitation ullamco laboris nisi ut aliquip.</p>
  <p class="tx abs" style="left:102px;top:89px;width:262px;border-bottom:.5px solid #ccc;padding-bottom:2px">Lorem ipsum dolor sit amet, consectetur adipiscing elit, sed do eiusmod tempor incididunt ut labore et dolore magna aliqua. Ut enim ad minim veniam, quis nostrud exercitation ullamco laboris nisi ut aliquip.</p>
  <p class="tx abs" style="left:102px;top:118px;width:262px;border-bottom:.5px solid #ccc;padding-bottom:2px">Lorem ipsum dolor sit amet, consectetur adipiscing elit, sed do eiusmod tempor incididunt ut labore et dolore magna aliqua. Ut enim ad minim veniam, quis nostrud exercitation ullamco laboris nisi ut aliquip.</p>
  <p class="tx abs" style="left:102px;top:147px;width:262px;border-bottom:.5px solid #ccc;padding-bottom:2px">Lorem ipsum dolor sit amet, consectetur adipiscing elit, sed do eiusmod tempor incididunt ut labore et dolore magna aliqua. Ut enim ad minim veniam, quis nostrud exercitation ullamco laboris nisi ut aliquip.</p>
  <div class="foot"><div class="stripe"></div>Copyright © 2020 Terravera | All rights reserved</div>
</div>

<div class="slide c2 r6">
  <div class="bar"><h3>ADD YOUR AWESOME TITLE HERE</h3><small>HERE ADD YOUR TITLE</small><div class="brand"><i></i>TERRAVERA</div><div class="stripe"></div></div>
  <div class="abs" style="left:28px;top:47px;width:100px"><p class="hd" style="font-weight:600">Lorem ipsum</p><p class="tx">• Lorem ipsum dolor sit amet, consectetur adipiscing elit.<br>• Lorem ipsum dolor sit amet, consectetur adipiscing elit. Maecas porttitor congue massa.</p></div>
  <div class="abs" style="left:144px;top:47px;width:100px"><p class="hd" style="font-weight:600">Lorem ipsum</p><p class="tx">• Lorem ipsum dolor sit amet, consectetur adipiscing elit.<br>• Lorem ipsum dolor sit amet, consectetur adipiscing elit. Maecas porttitor congue massa.</p></div>
  <div class="abs" style="left:260px;top:47px;width:100px"><p class="hd" style="font-weight:600">Lorem ipsum</p><p class="tx">• Lorem ipsum dolor sit amet, consectetur adipiscing elit.<br>• Lorem ipsum dolor sit amet, consectetur adipiscing elit. Maecas porttitor congue massa.</p></div>
  <table class="grid-tab" style="left:16px;top:107px;width:353px">
    <tr><th>Text</th><th>Text</th><th>Text</th><th>Text</th><th style="background:var(--navy);color:#fff">TERRAVERA</th><th>Text</th></tr>
    <tr><td>Data</td><td>Data</td><td>Data</td><td>Data</td><td>Data</td><td>Data</td></tr>
    <tr><td>Data</td><td>Data</td><td>Data</td><td>Data</td><td>Data</td><td>Data</td></tr>
    <tr><td>Data</td><td>Data</td><td>Data</td><td>Data</td><td>Data</td><td>Data</td></tr>
    <tr><td>Data</td><td>Data</td><td>Data</td><td>Data</td><td>Data</td><td>Data</td></tr>
    <tr><td>Data</td><td>Data</td><td>Data</td><td>Data</td><td>Data</td><td>Data</td></tr>
  </table>
  <div class="foot"><div class="stripe"></div>Copyright © 2020 Terravera | All rights reserved</div>
</div>

<div class="slide c3 r6">
  <div class="bar"><h3>STATISTIC</h3><small>HERE ADD YOUR TITLE</small><div class="brand"><i></i>TERRAVERA</div><div class="stripe"></div></div>
  <p class="abs" style="left:0;right:0;top:45px;margin:0;text-align:center;font-size:14px;color:var(--navy);font-weight:500">Your awesome text here</p>
  <p class="tx abs" style="left:85px;top:66px;width:214px;text-align:center">Lorem Ipsum the printing and typesetting industry. Lorem Ipsum has been the industry's standard dummy text ever since the 1500s, when an unknown printer took a galley of type and scrambled it to make a type specimen book.</p>
  <svg class="abs" style="left:80px;top:103px" width="230" height="62" viewBox="0 0 230 62">
    <g fill="none" stroke-width="4"><circle cx="30" cy="31" r="26" stroke="#e3e5e8"/><circle cx="30" cy="31" r="26" stroke="#5db335" stroke-dasharray="81.7 163.4" transform="rotate(-90 30 31)"/>
    <circle cx="112" cy="31" r="26" stroke="#e3e5e8"/><circle cx="112" cy="31" r="26" stroke="#1d9ad6" stroke-dasharray="122.5 163.4" transform="rotate(-90 112 31)"/>
    <circle cx="194" cy="31" r="26" stroke="#e3e5e8"/><circle cx="194" cy="31" r="26" stroke="#f5a11c" stroke-dasharray="65.4 163.4" transform="rotate(-90 194 31)"/></g>
    <g font-family="Montserrat,sans-serif" font-size="10" font-weight="600" fill="#1b2b4b" text-anchor="middle"><text x="30" y="35">50%</text><text x="112" y="35">75%</text><text x="194" y="35">40%</text></g>
  </svg>
  <p class="tx abs" style="left:85px;top:170px;width:50px;text-align:center">Lorem ipsum dolor amet consectetur</p>
  <p class="tx abs" style="left:167px;top:170px;width:50px;text-align:center">Lorem ipsum dolor amet consectetur</p>
  <p class="tx abs" style="left:249px;top:170px;width:50px;text-align:center">Lorem ipsum dolor amet consectetur</p>
  <div class="foot"><div class="stripe"></div>Copyright © 2020 Terravera | All rights reserved</div>
</div>

<!-- row 7 -->
<div class="slide c1 r7">
  <div class="brand dark"><i></i>TERRAVERA</div>
  <p class="abs" style="left:27px;top:53px;margin:0;font-size:11px;color:var(--navy);font-weight:500">STEPS TO SUCCESS</p>
  <p class="abs" style="left:52px;top:67px;margin:0;font-size:4.5px;color:#999">Write here a great subtitle</p>
  <div class="ph" style="left:196px;top:6px;width:58px;height:88px;background:linear-gradient(180deg,#e6f2d8,#f4f8ef)" role="img" aria-label="Pictogram of a figure climbing steps"></div>
  <div class="step" style="left:24px;top:165px;width:64px">01</div>
  <div class="step" style="left:93px;top:143px;width:64px">02</div>
  <div class="step" style="left:163px;top:121px;width:64px">03</div>
  <div class="step" style="left:233px;top:99px;width:64px">04</div>
  <div class="step" style="left:302px;top:77px;width:64px">05</div>
  <div class="abs" style="left:24px;top:179px;width:64px"><p class="hd" style="font-weight:500">Lorem ipsum dolor</p><p class="tx">Lorem ipsum dolor sit amet, consectetur adipiscing elit.</p></div>
  <div class="abs" style="left:96px;top:157px;width:64px"><p class="hd" style="font-weight:500">Lorem ipsum dolor</p><p class="tx">Lorem ipsum dolor sit amet, consectetur adipiscing elit.</p></div>
  <div class="abs" style="left:166px;top:135px;width:64px"><p class="hd" style="font-weight:500">Lorem ipsum dolor</p><p class="tx">Lorem ipsum dolor sit amet, consectetur adipiscing elit.</p></div>
  <div class="abs" style="left:236px;top:113px;width:64px"><p class="hd" style="font-weight:500">Lorem ipsum dolor</p><p class="tx">Lorem ipsum dolor sit amet, consectetur adipiscing elit.</p></div>
  <div class="abs" style="left:305px;top:91px;width:64px"><p class="hd" style="font-weight:500">Lorem ipsum dolor</p><p class="tx">Lorem ipsum dolor sit amet, consectetur adipiscing elit.</p></div>
  <div class="foot"><div class="stripe"></div>Copyright © 2020 Terravera | All rights reserved</div>
</div>

<div class="slide c2 r7">
  <div class="bar"><h3>STATISTIC AND TEXT</h3><small>HERE ADD YOUR TITLE</small><div class="brand"><i></i>TERRAVERA</div><div class="stripe"></div></div>
  <svg class="abs" style="left:14px;top:50px" width="230" height="150" viewBox="0 0 230 150">
    <g stroke="#eee" stroke-width=".5"><line x1="12" y1="10" x2="225" y2="10"/><line x1="12" y1="30" x2="225" y2="30"/><line x1="12" y1="50" x2="225" y2="50"/><line x1="12" y1="70" x2="225" y2="70"/><line x1="12" y1="90" x2="225" y2="90"/><line x1="12" y1="110" x2="225" y2="110"/></g>
    <g font-family="Montserrat,sans-serif" font-size="4" fill="#666"><text x="4" y="12">5</text><text x="4" y="32">4</text><text x="4" y="52">3</text><text x="4" y="72">2</text><text x="4" y="92">1</text><text x="4" y="112">0</text>
      <text x="30" y="120">Category 1</text><text x="82" y="120">Category 2</text><text x="136" y="120">Category 3</text><text x="190" y="120">Category 4</text>
      <text x="90" y="138">■ Series 1  ■ Series 2  ■ Series 3</text></g>
    <rect x="28" y="24" width="8" height="86" fill="#5db335"/><rect x="38" y="61" width="8" height="49" fill="#1d9ad6"/><rect x="48" y="70" width="8" height="40" fill="#fece3e"/>
    <rect x="82" y="60" width="8" height="50" fill="#5db335"/><rect x="92" y="22" width="8" height="88" fill="#1d9ad6"/><rect x="102" y="70" width="8" height="40" fill="#fece3e"/>
    <rect x="136" y="40" width="8" height="70" fill="#5db335"/><rect x="146" y="76" width="8" height="34" fill="#1d9ad6"/><rect x="156" y="50" width="8" height="60" fill="#fece3e"/>
    <rect x="190" y="20" width="8" height="90" fill="#5db335"/><rect x="200" y="50" width="8" height="60" fill="#1d9ad6"/><rect x="210" y="10" width="8" height="100" fill="#fece3e"/>
  </svg>
  <div class="abs" style="left:248px;top:40px;width:136px;height:162px;background:var(--panel)"></div>
  <div class="dot" style="left:264px;top:56px;width:18px;height:18px;background:var(--green);font-size:7px">✓</div>
  <div class="dot" style="left:264px;top:96px;width:18px;height:18px;background:var(--green);font-size:7px">✓</div>
  <div class="dot" style="left:264px;top:136px;width:18px;height:18px;background:var(--green);font-size:7px">✓</div>
  <div class="abs" style="left:290px;top:53px;width:80px"><p class="hd" style="font-weight:500">Project name</p><p class="tx">Lorem ipsum dolor sit amet, nec an dictas equidem appetere, ut has commune accommodare.</p></div>
  <div class="abs" style="left:290px;top:93px;width:80px"><p class="hd" style="font-weight:500">Project name</p><p class="tx">Lorem ipsum dolor sit amet, nec an dictas equidem appetere, ut has commune accommodare.</p></div>
  <div class="abs" style="left:290px;top:133px;width:80px"><p class="hd" style="font-weight:500">Project name</p><p class="tx">Lorem ipsum dolor sit amet, nec an dictas equidem appetere, ut has commune accommodare.</p></div>
  <div class="foot"><div class="stripe"></div>Copyright © 2020 Terravera | All rights reserved</div>
</div>

<div class="slide c3 r7">
  <div class="bar"><h3>ADD YOUR AWESOME TITLE HERE</h3><small>HERE ADD YOUR TITLE</small><div class="brand"><i></i>TERRAVERA</div><div class="stripe"></div></div>
  <div class="abs" style="left:37px;top:61px;width:310px;height:112px;background:var(--panel)"></div>
  <div class="abs" style="left:192px;top:61px;width:78px;height:112px;background:var(--navy)"></div>
  <div class="abs" style="left:37px;top:61px;width:310px;display:flex;font-size:5px;font-weight:600;color:#fff">
    <span style="width:77px;height:17px;line-height:17px;background:var(--navy);padding-left:5px;border-right:1px solid #fff">ADD YOUR TITLE</span>
    <span style="width:78px;height:17px;line-height:17px;background:var(--navy);padding-left:5px">ADD YOUR TITLE</span>
    <span style="width:78px;height:17px;line-height:17px;background:#fff;color:var(--navy);padding-left:5px;font-weight:700">TERRAVERA</span>
    <span style="width:77px;height:17px;line-height:17px;background:var(--navy);padding-left:5px">ADD YOUR TITLE</span>
  </div>
  <div class="abs" style="left:42px;top:84px;width:305px;display:flex;flex-wrap:wrap;row-gap:14px">
    <div style="width:77px;padding-right:6px"><p class="hd" style="font-weight:500">Project name</p><p class="tx">Lorem ipsum is simply dummy unknown printer took a galley of type.</p></div>
    <div style="width:78px;padding-right:6px"><p class="hd" style="font-weight:500">Project name</p><p class="tx">Lorem ipsum is simply dummy unknown printer took a galley of type.</p></div>
    <div style="width:78px;padding-right:6px;color:#fff"><p class="hd" style="font-weight:500;color:#fff">Project name</p><p class="tx" style="color:#cfd6e2">Lorem ipsum is simply dummy unknown printer took a galley of type.</p></div>
    <div style="width:72px"><p class="hd" style="font-weight:500">Project name</p><p class="tx">Lorem ipsum is simply dummy unknown printer took a galley of type.</p></div>
    <div style="width:77px;padding-right:6px"><p class="hd" style="font-weight:500">Project name</p><p class="tx">Lorem ipsum is simply dummy unknown printer took a galley of type.</p></div>
    <div style="width:78px;padding-right:6px"><p class="hd" style="font-weight:500">Project name</p><p class="tx">Lorem ipsum is simply dummy unknown printer took a galley of type.</p></div>
    <div style="width:78px;padding-right:6px;color:#fff"><p class="hd" style="font-weight:500;color:#fff">Project name</p><p class="tx" style="color:#cfd6e2">Lorem ipsum is simply dummy unknown printer took a galley of type.</p></div>
    <div style="width:72px"><p class="hd" style="font-weight:500">Project name</p><p class="tx">Lorem ipsum is simply dummy unknown printer took a galley of type.</p></div>
  </div>
  <div class="foot"><div class="stripe"></div>Copyright © 2020 Terravera | All rights reserved</div>
</div>

<!-- row 8 -->
<div class="slide c1 r8" style="background:var(--navy)">
  <div class="ph" style="inset:0;background:linear-gradient(180deg,#3a4a66,#2a3a58 45%,#7a6a58 75%,#3a3a40)" role="img" aria-label="Photograph of a wind turbine on a hillside at dusk"></div>
  <p class="abs" style="left:0;right:0;top:100px;margin:0;text-align:center;color:#fff;font-size:11px;font-weight:700">Why we need to do a climate risk assessment</p>
</div>

<div class="slide c2 r8">
  <div class="ph" style="left:0;top:0;width:112px;height:185px;background:linear-gradient(180deg,#e8f2dc,#fdf3d6)" role="img" aria-label="Illustration of a light bulb with a green plant sprouting from it"></div>
  <div class="abs" style="left:205px;top:28px;display:flex;gap:18px;font-size:3.6px;color:#555;text-align:center">
    <div><svg width="8" height="8" viewBox="0 0 8 8"><circle cx="4" cy="4" r="3.5" fill="#1b2b4b"/></svg><br>Social Media<br>@terravera</div>
    <div><svg width="8" height="8" viewBox="0 0 8 8"><rect x="0.5" y="1.5" width="7" height="5" fill="none" stroke="#1b2b4b"/><path d="M.5 1.5 4 4.5 7.5 1.5" fill="none" stroke="#1b2b4b" stroke-width=".7"/></svg><br>Email<br>info@terravera.co</div>
    <div><svg width="8" height="8" viewBox="0 0 8 8"><path d="M2 1l1.5 2-1 1a4 4 0 0 0 1.5 1.5l1-1 2 1.5-1 1.5C3 7 1 5 .5 2z" fill="#1b2b4b"/></svg><br>Phone<br>+1 555 0142</div>
    <div><svg width="8" height="8" viewBox="0 0 8 8"><circle cx="4" cy="4" r="3.3" fill="none" stroke="#1b2b4b" stroke-width=".8"/><path d="M.7 4h6.6M4 .7v6.6" stroke="#1b2b4b" stroke-width=".6"/></svg><br>Website<br>www.terravera.co</div>
  </div>
  <div class="brand dark" style="left:250px;right:auto;top:66px;font-size:10px"><i style="width:11px;height:11px"></i>TERRAVERA</div>
  <p class="abs" style="left:102px;top:112px;margin:0;font-size:14px;color:var(--navy);font-weight:500;line-height:1.35">LINKING<br>SCIENCE AND<br>DECISION-MAKING</p>
  <div class="abs" style="left:0;right:0;bottom:0;height:14px;background:var(--navy)"></div>
</div>

</body>
</html>
```